Capacity building in Resource Management

Need design of a business card (later to be completed by letterhead and webdesign in same fashion) for a professional who works in the field of capacity building of professionals in mostly developing countries in the field waste/resource management, waste prevention/reduction, cleaner production, stakeholders involvement, etc.
Info on business cards is to include provided logo, info in provided file and picture.

Industry/Entity Type

Business

Contact Information for Business Card

White background

Font styles to use
Sans Serif

Colors

Designer to choose colors to be used in the design.

```html
<!DOCTYPE html>
<html lang="en">
<head>
<meta charset="utf-8">
<title>Terrava business card</title>
<link href="https://fonts.googleapis.com/css2?family=Raleway:wght@400;500;700;800&display=swap" rel="stylesheet">
<style>
  :root {
    --backdrop: #dadada;
    --paper: #ffffff;
    --green: #4f7f35;
    --green-dark: #2f5a20;
    --green-deep: #3a6327;
    --ink: #222222;
    --back-text: #e9f0e4;
    --photo-light: #c9b9a8;
    --photo-dark: #8a6f5c;
  }
  * { margin: 0; padding: 0; box-sizing: border-box; }
  html, body { width: 1200px; height: 545px; overflow: hidden; }
  body {
    background: var(--backdrop);
    font-family: "Raleway", Arial, sans-serif;
    position: relative;
  }
  .card {
    position: absolute;
    width: 518px;
    height: 302px;
    border-radius: 28px;
    overflow: hidden;
  }
  .card-front { left: 67px; top: 118px; background: var(--paper); }
  .card-back {
    left: 620px; top: 118px; width: 515px; height: 300px;
    background: linear-gradient(135deg, #3a6528 0%, #4b7b34 60%, #50823a 100%);
    color: var(--back-text);
  }

  .holder-name {
    position: absolute; left: 30px; top: 37px;
    font-weight: 800; font-size: 15px; letter-spacing: 0.4px;
    color: var(--green-dark);
  }

  .brand {
    position: absolute; right: 18px; top: 54px;
    display: flex; align-items: center; gap: 10px;
  }
  .brand-mark { width: 22px; height: 22px; background: var(--green); flex: none; }
  .brand-name {
    font-weight: 800; font-size: 30px; line-height: 1;
    color: var(--green-dark);
  }

  .contact-list, .social-list { position: absolute; left: 30px; list-style: none; }
  .contact-list { top: 112px; color: var(--ink); }
  .social-list { top: 199px; color: #ffffff; }
  .contact-list li, .social-list li {
    display: flex; align-items: center; height: 18px;
    font-size: 13px; font-weight: 500;
  }
  .contact-list svg, .social-list svg { width: 15px; height: 15px; margin-right: 7px; flex: none; }

  .divider { position: absolute; left: 0; right: 0; top: 179px; height: 3px; background: var(--green); }
  .band { position: absolute; left: 0; right: 0; top: 185px; bottom: 0; background: var(--green); }
  .address-strip { position: absolute; left: 0; bottom: 0; width: 100%; height: 36px; }
  .address {
    position: absolute; left: 30px; bottom: 9px;
    display: flex; align-items: center; color: #ffffff;
    font-size: 13px; font-weight: 500;
  }
  .address svg { width: 15px; height: 15px; margin-right: 8px; }

  .portrait {
    position: absolute; left: 375px; top: 137px; width: 126px; height: 156px;
    background: linear-gradient(160deg, var(--photo-light) 0%, #f4f1ec 55%, var(--photo-dark) 100%);
    border-radius: 60px 60px 0 0;
  }

  .focus-list { position: absolute; left: 41px; top: 73px; list-style: none; }
  .focus-list li { font-size: 15px; font-weight: 500; height: 22px; letter-spacing: 0.2px; }
  .focus-list .focus-title { font-weight: 700; color: #ffffff; height: 24px; }
</style>
</head>
<body>

<section class="card card-front">
  <div class="band"></div>
  <div class="divider"></div>
  <svg class="address-strip" viewBox="0 0 518 36" preserveAspectRatio="none" aria-hidden="true">
    <path d="M0 0 H290 C305 0 310 4 318 14 C326 26 332 36 348 36 H0 Z" fill="var(--green-deep)"/>
  </svg>

  <h1 class="holder-name">JONAS R. VELDEN</h1>

  <div class="brand">
    <span class="brand-mark" aria-hidden="true"></span>
    <span class="brand-name">Terrava</span>
  </div>

  <ul class="contact-list">
    <li>
      <svg viewBox="0 0 16 16"><circle cx="8" cy="8" r="8" fill="var(--green)"/><path d="M5.2 4.2l1.5-.3.8 2-1 .8c.5 1.2 1.4 2.1 2.6 2.6l.8-1 2 .8-.3 1.5c-3.6.2-6.6-2.8-6.4-6.4z" fill="#fff"/></svg>
      +49 1500 214 7730 (also whatsapp)
    </li>
    <li>
      <svg viewBox="0 0 16 16"><circle cx="8" cy="8" r="8" fill="var(--green)"/><rect x="4" y="5" width="8" height="6" fill="#fff"/><path d="M4 5l4 3.2L12 5" stroke="var(--green)" stroke-width="1" fill="none"/></svg>
      jonas.velden@terrava.com
    </li>
    <li>
      <svg viewBox="0 0 16 16"><circle cx="8" cy="8" r="8" fill="var(--green)"/><circle cx="8" cy="8" r="4.2" fill="none" stroke="#fff" stroke-width="1.1"/><path d="M3.8 8h8.4M8 3.8c-2 2.4-2 6 0 8.4M8 3.8c2 2.4 2 6 0 8.4" stroke="#fff" stroke-width="0.9" fill="none"/></svg>
      www.terrava.com
    </li>
  </ul>

  <ul class="social-list">
    <li><svg viewBox="0 0 16 16"><circle cx="8" cy="8" r="8" fill="#fff"/></svg>@jonasvelden</li>
    <li><svg viewBox="0 0 16 16"><circle cx="8" cy="8" r="8" fill="#fff"/></svg>velden2010</li>
    <li><svg viewBox="0 0 16 16"><circle cx="8" cy="8" r="8" fill="#fff"/></svg>Jonas Velden</li>
  </ul>

  <div class="address">
    <svg viewBox="0 0 16 16"><circle cx="8" cy="8" r="8" fill="#fff"/><path d="M8 3.5a3 3 0 0 1 3 3c0 2.2-3 5.8-3 5.8S5 8.7 5 6.5a3 3 0 0 1 3-3z" fill="var(--green-deep)"/><circle cx="8" cy="6.5" r="1.1" fill="#fff"/></svg>
    Am Lindenhof 12, 10117 Berlin, Germany
  </div>

  <div class="portrait" role="img" aria-label="Portrait photograph of the card holder in a white shirt"></div>
</section>

<section class="card card-back">
  <ul class="focus-list">
    <li class="focus-title">Resource Management</li>
    <li>... prevention/reuse/reduction/recycling</li>
    <li>... cleaner production/process optimization</li>
    <li>... institutional/legal issues</li>
    <li>... social, environmental, financial aspects</li>
    <li>... conceptual system selection</li>
    <li>... awareness/involvement</li>
  </ul>
</section>

</body>
</html>
```